Business Card Design

We are a business based in Sydney repairing and restoring timber windows. We mainly cater to residential home owners although sometimes work with larger building companies. We do a lot of work in heritage buildings though also cater to modern windows.
Our Logo is Black and Gold and were thinking of using a white card with only these two colours although we are open to any design suggestions. Check out our website for ideas.
Front of Card
Contact Information, Website & Business Name
Back of Card
Business Logo, website?
Target Market(s)
Home Owners
Industry/Entity Type
Residential
Contact Information for Business Card
Oakridge Sash Revivals
Marcus Pellow
0472 309 648
marcus@oakridgesashrevivals.example
www.oakridgesashrevivals.example
Look and feel

```html
<!DOCTYPE html>
<html lang="en">
<head>
<meta charset="utf-8">
<title>Oakridge Sash Revivals – Business Cards</title>
<link rel="stylesheet" href="https://fonts.googleapis.com/css2?family=Roboto+Condensed:ital,wght@0,300;0,500;0,700;1,300;1,500&display=swap">
<style>
  :root {
    --gold: #e0b613;
    --ink: #111111;
    --paper: #ffffff;
    --edge: #2a2a2a;
  }
  * { margin: 0; padding: 0; box-sizing: border-box; }
  html, body { width: 1200px; height: 1000px; overflow: hidden; background: var(--paper); }
  body { position: relative; font-family: "Roboto Condensed", "Arial Narrow", sans-serif; color: var(--ink); }

  .card { position: absolute; width: 540px; height: 332px; }
  .card--white { background: var(--paper); border: 1px solid var(--edge); }
  .card--gold { background: var(--gold); }

  .card--logo-white { left: 42px; top: 132px; }
  .card--info-white { left: 616px; top: 133px; }
  .card--logo-gold { left: 42px; top: 528px; }
  .card--info-gold { left: 616px; top: 529px; }

  .rule { position: absolute; width: 57px; height: 3px; background: var(--gold); }
  .card--gold .rule { background: var(--ink); }
  .rule--top { top: 46px; }
  .rule--bottom { top: 277px; }
  .card--logo-white .rule, .card--logo-gold .rule { left: 46px; }
  .card--info-white .rule, .card--info-gold .rule { right: 58px; }

  .brand {
    position: absolute; left: 47px; top: 90px;
    font-weight: 500; font-size: 40px; line-height: 43px;
    letter-spacing: 0.2px; color: var(--ink);
  }
  .brand span { display: block; }

  .contact {
    position: absolute; right: 56px; top: 96px;
    text-align: right; color: var(--ink);
  }
  .contact__company { font-weight: 700; font-size: 15px; line-height: 18px; text-transform: uppercase; letter-spacing: 0.2px; }
  .contact__name { font-weight: 500; font-style: italic; font-size: 15px; line-height: 20px; }
  .contact__phone { font-weight: 700; font-size: 20px; line-height: 24px; margin-top: 15px; letter-spacing: 0.3px; }
  .contact__web { font-weight: 300; font-style: italic; font-size: 15px; line-height: 20px; margin-top: 17px; }
</style>
</head>
<body>

  <section class="card card--white card--logo-white" aria-label="Card back, white">
    <div class="rule rule--top"></div>
    <p class="brand"><span>Oakridge</span><span>Sash</span><span>Revivals</span></p>
    <div class="rule rule--bottom"></div>
  </section>

  <section class="card card--white card--info-white" aria-label="Card front, white">
    <div class="rule rule--top"></div>
    <div class="contact">
      <p class="contact__company">Oakridge Sash Revivals</p>
      <p class="contact__name">Marcus Pellow</p>
      <p class="contact__phone">0472 309 648</p>
      <p class="contact__web">marcus@oakridgesashrevivals.example<br>www.oakridgesashrevivals.example</p>
    </div>
    <div class="rule rule--bottom"></div>
  </section>

  <section class="card card--gold card--logo-gold" aria-label="Card back, gold">
    <div class="rule rule--top"></div>
    <p class="brand"><span>Oakridge</span><span>Sash</span><span>Revivals</span></p>
    <div class="rule rule--bottom"></div>
  </section>

  <section class="card card--gold card--info-gold" aria-label="Card front, gold">
    <div class="rule rule--top"></div>
    <div class="contact">
      <p class="contact__company">Oakridge Sash Revivals</p>
      <p class="contact__name">Marcus Pellow</p>
      <p class="contact__phone">0472 309 648</p>
      <p class="contact__web">marcus@oakridgesashrevivals.example<br>www.oakridgesashrevivals.example</p>
    </div>
    <div class="rule rule--bottom"></div>
  </section>

</body>
</html>
```